Business card for Luxury Portable Restroom Trailer company

We are a Luxury Portable Restroom Trailer Company Called PELIKAR HIRES. Based in Orange County California. We provide portable restroom trailers for events, such as, Weddings, Concerts, Charity events, Sporting events, Tournaments, Corporate events, ect. We rent and Sell the Luxury restrooms. Our colors are white, grey, and Orange. As you will see in the logo we uploaded.
There are 2 people in the company so the names and titles will change for the 3 people but card will remain the same. Here is the information for each Person: Dennis Moyle CFO 555 018-3647
next Person: Wesley Tanford VP 555 018-3647
Next Person: Miles Tanford CEO 555 018-3647
Information to include on the card: Luxury Restroom Trailers Rental and Sales. Weddings, Concerts, Charity, Sporting and Corp. Events.

```html
<!DOCTYPE html>
<html lang="en">
<head>
<meta charset="utf-8">
<title>Pelikar Hires – Business Card</title>
<link href="https://fonts.googleapis.com/css2?family=Montserrat:wght@400;500;700;800&display=swap" rel="stylesheet">
<style>
  :root {
    --orange: #e8702a;
    --orange-deep: #dc541b;
    --grey-dark: #4a4a4c;
    --text: #4d4d4f;
    --card: #f4f4f4;
    --backdrop: #d9d9db;
  }
  * { box-sizing: border-box; margin: 0; padding: 0; }
  html, body { width: 1200px; height: 1200px; overflow: hidden; }
  body {
    background: var(--backdrop);
    font-family: "Montserrat", sans-serif;
    color: var(--text);
    position: relative;
  }
  .card {
    position: absolute;
    left: 250px;
    width: 700px;
    height: 400px;
    background: linear-gradient(135deg, #ffffff 0%, var(--card) 100%);
    box-shadow: 0 6px 18px rgba(0,0,0,0.18);
    overflow: hidden;
  }
  .card--back { top: 150px; }
  .card--front { top: 650px; }

  .brand {
    position: absolute;
    left: 190px;
    display: flex;
    align-items: center;
    gap: 12px;
    font-weight: 800;
    font-size: 40px;
    line-height: 1;
    letter-spacing: 1px;
    color: var(--orange);
    white-space: nowrap;
  }
  .brand__square { width: 26px; height: 26px; background: var(--orange); flex: none; }
  .card--back .brand { top: 60px; }
  .card--front .brand { top: 55px; }

  .services-tag {
    position: absolute;
    left: 340px; top: 140px;
    width: 180px; height: 44px;
    background: var(--orange);
    color: #fff;
    font-size: 26px;
    font-weight: 400;
    display: flex; align-items: center; justify-content: center;
  }
  .service-list {
    position: absolute;
    list-style: none;
    font-size: 17px;
    line-height: 1.55;
    white-space: nowrap;
  }
  .service-list li::before {
    content: "";
    display: inline-block;
    width: 6px; height: 6px; border-radius: 50%;
    background: var(--orange);
    margin-right: 9px;
    vertical-align: middle;
  }
  .service-list--left { left: 50px; top: 140px; }
  .service-list--right { left: 360px; top: 240px; }

  .person { position: absolute; left: 50px; top: 140px; width: 240px; text-align: center; }
  .person__name { font-size: 30px; font-weight: 700; color: var(--orange); white-space: nowrap; }
  .person__title { font-size: 18px; margin-top: 2px; }
  .divider {
    position: absolute; left: 320px; top: 148px;
    width: 2px; height: 62px; background: var(--grey-dark);
  }
  .contact { position: absolute; left: 345px; top: 150px; font-size: 18px; line-height: 1.7; white-space: nowrap; }
  .contact__row { display: flex; align-items: center; gap: 10px; }
  .contact__row svg { width: 16px; height: 16px; fill: var(--orange); }
  .address {
    position: absolute; left: 50px; top: 232px;
    font-size: 16px; white-space: nowrap;
  }

  .swoosh { position: absolute; left: 0; top: 0; width: 700px; height: 400px; }
  .website {
    position: absolute; right: 40px; top: 364px;
    font-size: 20px; color: #fff; font-weight: 500;
  }
</style>
</head>
<body>

<section class="card card--back">
  <div class="brand"><span class="brand__square"></span>PELIKAR HIRES</div>
  <div class="services-tag">Services</div>
  <ul class="service-list service-list--left">
    <li>Luxury Restroom</li>
    <li>Trailers Rental and Sales</li>
    <li>Weddings</li>
  </ul>
  <ul class="service-list service-list--right">
    <li>Concerts</li>
    <li>Charity</li>
    <li>Sporting and Corp. Events</li>
  </ul>
</section>

<section class="card card--front">
  <svg class="swoosh" viewBox="0 0 700 400" aria-hidden="true">
    <path d="M0 282 C180 288 330 330 440 400 L0 400 Z" fill="var(--grey-dark)"/>
    <path d="M0 294 C200 298 420 335 600 400 L0 400 Z" fill="#f4f4f4"/>
    <path d="M0 302 C240 312 500 340 700 352 L700 400 L0 400 Z" fill="var(--orange-deep)"/>
  </svg>
  <div class="brand"><span class="brand__square"></span>PELIKAR HIRES</div>
  <div class="person">
    <div class="person__name">Dennis Moyle</div>
    <div class="person__title">CFO</div>
  </div>
  <div class="divider"></div>
  <div class="contact">
    <div class="contact__row">
      <svg viewBox="0 0 24 24"><path d="M6.6 10.8a15.1 15.1 0 0 0 6.6 6.6l2.2-2.2a1 1 0 0 1 1-.25 11.4 11.4 0 0 0 3.6.57 1 1 0 0 1 1 1V20a1 1 0 0 1-1 1A17 17 0 0 1 3 4a1 1 0 0 1 1-1h3.5a1 1 0 0 1 1 1c0 1.25.2 2.45.57 3.57a1 1 0 0 1-.25 1z"/></svg>
      <span>555 018-3647</span>
    </div>
    <div class="contact__row">
      <svg viewBox="0 0 24 24"><path d="M2 5h20v14H2z M2 5l10 8 10-8" stroke="#fff" stroke-width="1.5"/></svg>
      <span>info@pelikarhires.com</span>
    </div>
  </div>
  <div class="address">4710 Harbor Crest Road Laguna Hills California 92653</div>
  <div class="website">www.pelikarhires.com</div>
</section>

</body>
</html>
```